Health care technology software systems

We have a solid logo. We have company colors that will need to be used as well. We just need a great business card design. We sell to health plans but want to be modern

Target Market(s)

Health technology sector selling into Health Plans

Industry/Entity Type

Health Care Technology

Contact Information for Business Card

Name, title, address, phone number, email

Requirements
Must have
• Use of Parvexa corporate colors - Uploaded w/ our logos

```html
<!DOCTYPE html>
<html lang="en">
<head>
<meta charset="utf-8">
<title>Parvexa Business Card</title>
<link href="https://fonts.googleapis.com/css2?family=Poppins:wght@200;400;600&family=Montserrat:wght@600&display=swap" rel="stylesheet">
<style>
  :root {
    --backdrop: #f2f2f4;
    --navy: #19214f;
    --royal: #3d56a0;
    --lime: #8cc63f;
    --sky: #35a8de;
    --paper: #f3f3f5;
    --ink: #3a3a3c;
    --white: #ffffff;
  }
  * { margin: 0; padding: 0; box-sizing: border-box; }
  html, body { width: 1200px; height: 1000px; overflow: hidden; }
  body { background: var(--backdrop); position: relative; font-family: "Poppins", sans-serif; }

  .card { position: absolute; width: 463px; height: 265px; overflow: hidden; }
  .card-front { left: 308px; top: 188px; background: var(--navy); }
  .card-back { left: 383px; top: 488px; background: var(--paper); }
  .card-waves { position: absolute; inset: 0; width: 100%; height: 100%; }

  .front-wordmark {
    position: absolute; left: 0; right: 0; top: 128px;
    text-align: center; color: var(--white);
    font-weight: 200; font-size: 40px; letter-spacing: 1px; line-height: 1;
  }

  .back-wordmark {
    position: absolute; right: 38px; top: 58px;
    color: var(--royal); font-weight: 600; font-size: 22px; line-height: 1;
  }
  .holder-name {
    position: absolute; left: 54px; top: 50px;
    color: var(--ink); font-weight: 600; font-size: 25px; letter-spacing: 1px; line-height: 1;
  }
  .holder-title {
    position: absolute; left: 54px; top: 83px;
    color: var(--ink); font-weight: 400; font-size: 15px; line-height: 1;
  }
  .contact-rail {
    position: absolute; left: 53px; top: 115px; width: 24px; height: 103px;
    background: var(--lime); border-radius: 12px;
  }
  .contact-rail svg { position: absolute; left: 0; top: 0; }
  .contact-line {
    position: absolute; left: 93px;
    color: var(--ink); font-family: "Montserrat", sans-serif; font-weight: 600;
    font-size: 12.5px; line-height: 16px;
  }
  .contact-address { top: 124px; }
  .contact-phone { top: 165px; }
  .contact-email { top: 193px; }
</style>
</head>
<body>

  <section class="card card-front" aria-label="Card front">
    <svg class="card-waves" viewBox="0 0 463 265" aria-hidden="true">
      <path d="M0,195 Q130,262 305,205 L305,265 L0,265 Z" fill="var(--lime)"/>
      <path d="M0,265 C150,262 240,250 282,226 C350,186 392,144 463,150 L463,265 Z" fill="var(--royal)"/>
    </svg>
    <div class="front-wordmark">parvexa</div>
  </section>

  <section class="card card-back" aria-label="Card back">
    <svg class="card-waves" viewBox="0 0 464 265" aria-hidden="true">
      <path d="M0,265 C120,258 238,246 280,228 C340,200 380,142 464,150 L464,265 Z" fill="var(--sky)"/>
    </svg>
    <div class="back-wordmark">parvexa</div>
    <h1 class="holder-name">MARA ELLISON</h1>
    <p class="holder-title">General Manager</p>

    <div class="contact-rail">
      <svg width="24" height="103" viewBox="0 0 24 103" aria-hidden="true">
        <path d="M12,14 a4,4 0 0 1 4,4 c0,3 -4,7 -4,7 c0,0 -4,-4 -4,-7 a4,4 0 0 1 4,-4 z" fill="none" stroke="var(--white)" stroke-width="1.4"/>
        <circle cx="12" cy="18" r="1.3" fill="var(--white)"/>
        <path d="M9,53 c0,4 3,7 7,7 l1,-2 -2,-1.5 -1,1 c-1.5,-0.7 -2.5,-1.7 -3.2,-3.2 l1,-1 -1.5,-2 z" fill="var(--white)"/>
        <rect x="8" y="84" width="8" height="5.5" rx="1" fill="var(--white)"/>
      </svg>
    </div>
    <p class="contact-line contact-address">1450 W Harbor Point Dr<br>Cedar Bay, Florida(FL), 34120</p>
    <p class="contact-line contact-phone">905-555-0142</p>
    <p class="contact-line contact-email">maraellison@parvexa.com</p>
  </section>

</body>
</html>
```